Mobile technology Business Card Design Project

We need a business card design for our company based in Sydeny Australia, that takes a company's desktop sites and creates a mobile site compatible to all mobile/smartphone devices. This allows greater ease of use and generally faster business conversion than customers using a desktop site.
Our company is called VelqCore but we refer to it as Velq Corestreams. If this could be represented somewhere on the business card that would be great.
Am open to suggestions regarding the colours but a high tech  theme would be good.
Happy bidding!

Target Market(s)
Business owner that has a website and is reasonably savvy regarding online/mobile marketing.
Industry/Entity Type
Business
Requirements
Must have
- Business card details:
Director Peter Langwade
Address: 5/41 Dunmore rd, Kelbrook. 2087
Email: tbc
Web: www.velqcore.com.au
The cards need to have two different names for the two directors.
Gregory Halvane & Peter Langwade (two separate business cards)

```html
<!DOCTYPE html>
<html lang="en">
<head>
<meta charset="utf-8">
<title>VelqCore Business Card Concepts</title>
<link rel="stylesheet" href="https://fonts.googleapis.com/css2?family=Play&family=Ubuntu:wght@500;700&family=Ubuntu+Condensed&display=swap">
<style>
  :root {
    --page: #ffffff;
    --frame: #8fa3ad;
    --brand-blue: #4a9df7;
    --brand-blue-soft: #5eaaf8;
    --brand-orange: #f26122;
    --brand-orange-soft: #f2781e;
    --heading-grey: #9c9ca2;
    --ink: #111111;
    --ink-light: #ffffff;
  }
  * { box-sizing: border-box; margin: 0; padding: 0; }
  html, body {
    width: 1200px;
    height: 800px;
    overflow: hidden;
    background: var(--page);
  }
  .sheet {
    position: relative;
    width: 1200px;
    height: 800px;
  }
  .card {
    position: absolute;
    width: 545px;
    height: 313px;
    border: 3px solid var(--frame);
    overflow: hidden;
  }
  .card--front { left: 15px; top: 47px; background: var(--page); }
  .card--blue { left: 642px; top: 47px; background: var(--brand-blue); }
  .card--white { left: 15px; top: 441px; background: var(--page); }
  .card--orange { left: 642px; top: 441px; background: var(--brand-orange); }

  .brand {
    position: absolute;
    left: 0; right: 0; top: 34px;
    display: flex;
    flex-direction: column;
    align-items: center;
  }
  .brand__dot {
    width: 168px;
    height: 168px;
    border-radius: 50%;
    background: var(--brand-blue);
  }
  .brand__name {
    margin-top: 18px;
    font-family: "Ubuntu", sans-serif;
    font-weight: 700;
    font-size: 34px;
    line-height: 1;
    color: var(--ink);
  }
  .brand__tagline {
    margin-top: 12px;
    font-family: "Ubuntu", sans-serif;
    font-weight: 700;
    font-size: 16px;
    line-height: 1;
    color: var(--brand-orange);
  }

  .card__heading {
    position: absolute;
    left: 0; right: 0; top: 2px;
    text-align: center;
    font-family: "Play", sans-serif;
    font-weight: 400;
    font-size: 54px;
    line-height: 1.1;
    white-space: nowrap;
  }
  .card--blue .card__heading { color: var(--brand-blue-soft); }
  .card--white .card__heading { color: var(--heading-grey); }
  .card--orange .card__heading { color: var(--brand-orange-soft); }

  .details {
    position: absolute;
    left: 0; right: 0; top: 113px;
    text-align: center;
    font-family: "Ubuntu Condensed", "Ubuntu", sans-serif;
    font-size: 26px;
    line-height: 34px;
    list-style: none;
  }
  .card--blue .details,
  .card--orange .details { color: var(--ink-light); }
  .card--white .details { color: var(--ink); }
</style>
</head>
<body>
<main class="sheet">
  <section class="card card--front">
    <div class="brand">
      <span class="brand__dot"></span>
      <span class="brand__name">VelqCore</span>
      <span class="brand__tagline">Making Sites Pocket Ready</span>
    </div>
  </section>

  <section class="card card--blue">
    <h2 class="card__heading">Velq Corestreams</h2>
    <ul class="details">
      <li>Director Peter Langwade</li>
      <li>5/41 Dunmore rd,</li>
      <li>Kelbrook. 2087</li>
      <li>www.velqcore.com.au</li>
    </ul>
  </section>

  <section class="card card--white">
    <h2 class="card__heading">Velq Corestreams</h2>
    <ul class="details">
      <li>Director Peter Langwade</li>
      <li>5/41 Dunmore rd,</li>
      <li>Kelbrook. 2087</li>
      <li>www.velqcore.com.au</li>
    </ul>
  </section>

  <section class="card card--orange">
    <h2 class="card__heading">Velq Corestreams</h2>
    <ul class="details">
      <li>Director Peter Langwade</li>
      <li>5/41 Dunmore rd,</li>
      <li>Kelbrook. 2087</li>
      <li>www.velqcore.com.au</li>
    </ul>
  </section>
</main>
</body>
</html>
```